Juniper Crest Rehab logo and business cards

We need business cards for a company located in Las Vegas Nevada. We are the leaders in comprehensive outpatient cardiopulmonary rehab. We offer physical therapy, cardiac rehab, and pulmonary rehab. We are named after Juniper Crest here in Nevada and would like the business card to somehow feature a beautiful picture of the mountain. I want a captivating modern card that people will remember.

Target Market(s)

Pulmonologists, cardiologists, surgeons, hospitals, clinics, physical therapists, orthopedists, allergists, respiratory therapists, people who could use our services.

Industry/Entity Type

Rehabilitation

Contact Information for Business Card

Our name, slogan, address, individuals name, title, phone, fax, direct number if applicable, individuals personal email, website

Logo Text

Juniper Crest Rehab: Leader in comprehensive outpatient cardiopulmonary rehab

Font styles to use
Serif

Colors
85cae6
33b8a4
00a990
0692cd
3276b5
0255a3
b2b2b2
ec1f27
f04a50

Requirements
Must have
• Address: 4912 Copper Wren Rd, Ste 310 Las Vegas NV 89145
• Phone: (702) 555 - 0148
• Fax: (702) 555 - 0193
• www.junipercrestrehab.example
• Individuals name, title, and direct line if applicable, and personal email
Nice to have
• modern, sleek, pretty, captivating

```html
<!DOCTYPE html>
<html lang="en">
<head>
<meta charset="utf-8">
<title>Juniper Crest Rehab – Business Cards</title>
<link rel="stylesheet" href="https://fonts.googleapis.com/css2?family=Raleway:wght@500;600;700;800&family=Noto+Sans:wght@400&display=swap">
<style>
  :root {
    --navy: #34365c;
    --navy-deep: #2b2d52;
    --paper: #ffffff;
    --backdrop: #ecebe9;
    --ink: #2e3052;
    --ink-soft: #3c3c4a;
    --frame: #d9dae6;
  }
  * { margin: 0; padding: 0; box-sizing: border-box; }
  html, body {
    width: 1200px; height: 800px; overflow: hidden;
    background: var(--backdrop);
  }
  .canvas {
    position: relative; width: 1200px; height: 800px;
    display: flex; flex-direction: column; align-items: center; justify-content: center; gap: 40px;
  }
  .card {
    position: relative; width: 620px; height: 340px;
    box-shadow: 0 6px 18px rgba(0,0,0,0.12);
  }

  /* Back of card */
  .card-back {
    background: linear-gradient(160deg, #3e4068 0%, var(--navy) 55%, var(--navy-deep) 100%);
  }
  .card-back .frame {
    position: absolute; inset: 14px;
    border: 1.5px solid var(--frame);
  }
  .card-back .brand {
    position: absolute; left: 0; right: 0; top: 128px;
    display: flex; align-items: center; justify-content: center; gap: 12px;
  }
  .card-back .brand-square {
    width: 14px; height: 14px; background: #ffffff;
  }
  .card-back .brand-name {
    font-family: "Raleway", sans-serif; font-weight: 600;
    font-size: 30px; color: #ffffff; letter-spacing: 0.3px;
  }
  .card-back .site {
    position: absolute; left: 0; right: 0; top: 212px; text-align: center;
    font-family: "Raleway", sans-serif; font-weight: 600;
    font-size: 17px; color: #e9e9f2; letter-spacing: 0.4px;
  }

  /* Front of card */
  .card-front { background: var(--paper); }
  .card-front .brand {
    position: absolute; left: 40px; top: 58px;
    display: flex; align-items: center; gap: 9px;
  }
  .card-front .brand-square {
    width: 12px; height: 12px; background: var(--ink);
  }
  .card-front .brand-name {
    font-family: "Raleway", sans-serif; font-weight: 600;
    font-size: 17px; color: var(--ink);
  }
  .person {
    position: absolute; left: 36px; top: 158px;
  }
  .person-name {
    font-family: "Raleway", sans-serif; font-weight: 800;
    font-size: 20px; color: var(--ink); letter-spacing: 0.3px;
  }
  .person-title {
    font-family: "Raleway", sans-serif; font-weight: 600;
    font-size: 10.5px; color: var(--ink); margin-top: 2px;
  }
  .site-band {
    position: absolute; left: 246px; right: 0; top: 162px; height: 26px;
    background: var(--ink);
    display: flex; align-items: center; padding-left: 40px;
    font-family: "Raleway", sans-serif; font-weight: 600;
    font-size: 15px; color: #ffffff; letter-spacing: 0.5px;
  }
  .contact-list {
    position: absolute; left: 38px; top: 222px; list-style: none;
  }
  .contact-item {
    display: flex; align-items: center; gap: 14px; height: 25px;
    font-family: "Noto Sans", sans-serif; font-size: 15px; color: var(--ink-soft);
  }
  .contact-icon { width: 14px; height: 14px; flex: none; }
</style>
</head>
<body>
<main class="canvas">

  <section class="card card-back" aria-label="Business card back">
    <div class="frame"></div>
    <div class="brand">
      <span class="brand-square"></span>
      <span class="brand-name">Juniper Crest Rehab</span>
    </div>
    <div class="site">www.junipercrestrehab.example</div>
  </section>

  <section class="card card-front" aria-label="Business card front">
    <div class="brand">
      <span class="brand-square"></span>
      <span class="brand-name">Juniper Crest Rehab</span>
    </div>

    <div class="person">
      <div class="person-name">TESSA LINDQVIST</div>
      <div class="person-title">Community Relations Specialist</div>
    </div>

    <div class="site-band">www.junipercrestrehab.example</div>

    <ul class="contact-list">
      <li class="contact-item">
        <svg class="contact-icon" viewBox="0 0 14 14" aria-hidden="true">
          <rect x="3" y="0.8" width="8" height="12.4" rx="1.3" fill="none" stroke="#2e3052" stroke-width="1.5"/>
          <rect x="5.5" y="10.6" width="3" height="1" fill="#2e3052"/>
        </svg>
        <span>(702) 555 - 0148</span>
      </li>
      <li class="contact-item">
        <svg class="contact-icon" viewBox="0 0 14 14" aria-hidden="true">
          <rect x="3.5" y="0.8" width="7" height="4" fill="#2e3052"/>
          <rect x="0.5" y="5" width="13" height="5.5" rx="1" fill="#2e3052"/>
          <rect x="3.5" y="8.5" width="7" height="4.7" fill="#fff" stroke="#2e3052" stroke-width="1.2"/>
        </svg>
        <span>(702) 555 - 0193</span>
      </li>
      <li class="contact-item">
        <svg class="contact-icon" viewBox="0 0 14 14" aria-hidden="true">
          <path d="M7 0.5a4.6 4.6 0 0 0-4.6 4.6C2.4 8.6 7 13.5 7 13.5s4.6-4.9 4.6-8.4A4.6 4.6 0 0 0 7 0.5z" fill="#2e3052"/>
          <circle cx="7" cy="5.1" r="1.7" fill="#fff"/>
        </svg>
        <span>4912 Copper Wren Rd, Ste 310 Las Vegas NV 89145</span>
      </li>
    </ul>
  </section>

</main>
</body>
</html>
```